Contemporary Media Company with Logo Needs Business Card Design

Need a modern card design for a full service digital media company using the logo included. Also want the info below on the card. Probably list the services on the card back to save space for the front. Want something contemporary to impress prospective clients. You may want to submit both a somewhat more conservative design, and then a more wild one.
General Info: (this phrase need not be on the card)
Tod Parvin
Founder and CEO
949-628-4513
tod@lumavantstudio.example
lumavantstudio.example
Services: (this word need not be on the card)
Content & Experience Strategy
Brand Development
Search Engine Optimization
Website Design
Website Operation
Social Media Integration
Complete Video Solutions
Industry/Entity Type
Business
Contact Information for Business Card
Tod Parvin
Founder and CEO
949-628-4513
tod@lumavantstudio.example
lumavantstudio.example
Brand Development
Website Design
Website Operation
Social Media Integration
Complete Video Solutions
Look and feel

```html
<!DOCTYPE html>
<html lang="en">
<head>
<meta charset="utf-8">
<title>Lumavant Studio — Business Card</title>
<link href="https://fonts.googleapis.com/css2?family=Exo+2:wght@400;500;600;700&display=swap" rel="stylesheet">
<style>
  :root {
    --bg: #e9e6e1;
    --card: #ffffff;
    --orange: #ec6f22;
    --orange-light: #f28a30;
    --amber: #f3ab1f;
    --grey-dark: #5f6062;
    --grey-mid: #8a8b8d;
    --grey-light: #b9babb;
    --ink: #4a4b4d;
  }
  * { box-sizing: border-box; margin: 0; padding: 0; }
  html, body { width: 1200px; height: 900px; overflow: hidden; }
  body {
    background: var(--bg);
    font-family: "Exo 2", "Helvetica Neue", Arial, sans-serif;
    color: var(--ink);
    position: relative;
  }
  .card {
    position: absolute;
    width: 640px;
    height: 366px;
    background: var(--card);
    box-shadow: 0 10px 30px rgba(0,0,0,0.18);
    overflow: hidden;
  }
  .card--front { left: 70px; top: 60px; }
  .card--back { left: 490px; top: 474px; }

  .front-band {
    position: absolute; right: 0; top: 0;
    width: 230px; height: 366px;
  }
  .brand {
    position: absolute;
    display: flex; align-items: center; gap: 14px;
  }
  .brand-square { width: 26px; height: 26px; background: var(--orange); }
  .brand-name {
    font-weight: 500; font-size: 36px; letter-spacing: 4px;
    color: var(--grey-dark); text-transform: uppercase; line-height: 1;
  }
  .card--front .brand { left: 48px; top: 96px; }

  .contact { position: absolute; left: 48px; bottom: 44px; }
  .contact-name {
    font-weight: 700; font-size: 22px; letter-spacing: 1.5px;
    text-transform: uppercase; color: var(--grey-dark);
  }
  .contact-role {
    font-size: 13px; letter-spacing: 1px; text-transform: uppercase;
    color: var(--orange); margin-bottom: 14px;
  }
  .contact-line {
    display: flex; align-items: center; gap: 10px;
    font-size: 16px; color: var(--grey-dark); margin-top: 5px;
  }
  .contact-icon { width: 16px; height: 16px; flex: none; }

  .back-shape { position: absolute; left: 0; top: 0; width: 300px; height: 200px; }
  .card--back .brand { right: 44px; top: 60px; }
  .services { position: absolute; left: 44px; top: 150px; }
  .services-title {
    font-weight: 700; font-size: 18px; letter-spacing: 1.5px;
    text-transform: uppercase; color: var(--grey-dark); margin-bottom: 8px;
  }
  .services-cols { display: flex; gap: 40px; }
  .service-list { list-style: none; }
  .service-list li {
    display: flex; align-items: center; gap: 10px;
    font-size: 13px; letter-spacing: 1px; text-transform: uppercase;
    color: var(--grey-dark); line-height: 1.7;
  }
  .service-list li::before {
    content: ""; width: 9px; height: 9px; background: var(--orange); flex: none;
  }
</style>
</head>
<body>

<section class="card card--front" aria-label="Card front">
  <svg class="front-band" viewBox="0 0 230 366" aria-hidden="true">
    <rect x="150" y="0" width="80" height="366" fill="var(--orange)"/>
    <rect x="120" y="0" width="30" height="366" fill="var(--amber)"/>
  </svg>

  <div class="brand">
    <span class="brand-square"></span>
    <span class="brand-name">Lumavant Studio</span>
  </div>

  <div class="contact">
    <p class="contact-name">Tod Parvin</p>
    <p class="contact-role">Founder and CEO</p>
    <p class="contact-line">
      <svg class="contact-icon" viewBox="0 0 16 16" aria-hidden="true">
        <rect width="16" height="16" rx="2" fill="var(--orange)"/>
        <path d="M5 3.5l2 2-1 1.2c.6 1.3 1.6 2.3 2.9 2.9l1.2-1 2 2-1.3 1.6C7.5 11.8 4.2 8.5 3.8 5z" fill="#fff"/>
      </svg>
      949-628-4513
    </p>
    <p class="contact-line">
      <svg class="contact-icon" viewBox="0 0 16 16" aria-hidden="true">
        <rect width="16" height="16" rx="2" fill="var(--grey-dark)"/>
        <rect x="3" y="4.5" width="10" height="7" fill="none" stroke="#fff" stroke-width="1.2"/>
        <path d="M3 4.5l5 4 5-4" fill="none" stroke="#fff" stroke-width="1.2"/>
      </svg>
      tod@lumavantstudio.example
    </p>
    <p class="contact-line">
      <svg class="contact-icon" viewBox="0 0 16 16" aria-hidden="true">
        <rect width="16" height="16" rx="2" fill="var(--orange)"/>
        <circle cx="8" cy="8" r="4.5" fill="none" stroke="#fff" stroke-width="1.2"/>
        <path d="M3.5 8h9M8 3.5c-2 2.5-2 6.5 0 9M8 3.5c2 2.5 2 6.5 0 9" fill="none" stroke="#fff" stroke-width="1"/>
      </svg>
      lumavantstudio.example
    </p>
  </div>
</section>

<section class="card card--back" aria-label="Card back">
  <svg class="back-shape" viewBox="0 0 300 200" aria-hidden="true">
    <polygon points="0,0 260,0 150,120 0,120" fill="var(--grey-light)"/>
    <polygon points="0,0 150,120 0,120" fill="var(--grey-mid)"/>
  </svg>

  <div class="brand">
    <span class="brand-square"></span>
    <span class="brand-name">Lumavant Studio</span>
  </div>

  <div class="services">
    <h2 class="services-title">Services</h2>
    <div class="services-cols">
      <ul class="service-list">
        <li>Content &amp; Experience Strategy</li>
        <li>Brand Development</li>
        <li>Search Engine Optimization</li>
        <li>Website Design</li>
      </ul>
      <ul class="service-list">
        <li>Website Operation</li>
        <li>Social Media Integration</li>
        <li>Complete Video Solutions</li>
      </ul>
    </div>
  </div>
</section>

</body>
</html>
```